Kestrel Ridge Hides

I created the attached in quill mark. I would like the background to look like black leather and the text to be gold. Any other suggestions would be appreciated. Thank you
Please note: all text now should be white .... sorry Partners changed their mind
Please remember when submitting designs, this design is for a folded business card with printing on all 4 sides ..... thank you
Also, the front of the card must have the wording above the logo. These will be placed in the wallet ID pockets and I would like to be able to read the wording.
Printing
I would like a folded business card. I created one in Quillmark but don't know how to send it to you to apply the final touches.

```html
<!DOCTYPE html>
<html lang="en">
<head>
<meta charset="utf-8">
<title>Kestrel Ridge Hides – Card Inside</title>
<link href="https://fonts.googleapis.com/css2?family=Quicksand:wght@400&display=swap" rel="stylesheet">
<style>
  :root {
    --leather-dark: #121212;
    --leather-mid: #1e1e1e;
    --leather-edge: #080808;
    --text-white: #f2f2f2;
  }
  html, body {
    margin: 0;
    padding: 0;
    width: 1200px;
    height: 693px;
    overflow: hidden;
    background: var(--leather-dark);
  }
  .card {
    position: relative;
    width: 1200px;
    height: 693px;
    overflow: hidden;
  }
  .leather-surface {
    position: absolute;
    inset: 0;
    background: radial-gradient(ellipse at 50% 45%, var(--leather-mid) 0%, var(--leather-dark) 60%, var(--leather-edge) 100%);
  }
  .leather-grain {
    position: absolute;
    inset: 0;
    width: 1200px;
    height: 693px;
    display: block;
  }
  .leather-vignette {
    position: absolute;
    inset: 0;
    background: radial-gradient(ellipse at 50% 45%, rgba(0,0,0,0) 40%, rgba(0,0,0,0.55) 100%);
  }
  .card-message {
    position: absolute;
    top: 56px;
    left: 0;
    right: 0;
    margin: 0 auto;
    width: 1160px;
    text-align: center;
    color: var(--text-white);
    font-family: "Quicksand", sans-serif;
    font-weight: 400;
    font-size: 26px;
    line-height: 34px;
    letter-spacing: 0.1em;
  }
  .card-message p {
    margin: 0 0 34px;
  }
  .card-message .sign-off {
    margin: 0;
  }
</style>
</head>
<body>
  <main class="card">
    <div class="leather-surface" role="img" aria-label="Black leather grain background"></div>
    <svg class="leather-grain" viewBox="0 0 1200 693" aria-hidden="true">
      <defs>
        <filter id="pebble-grain" x="0" y="0" width="100%" height="100%">
          <feTurbulence type="fractalNoise" baseFrequency="0.07" numOctaves="2" seed="4" result="cells"/>
          <feColorMatrix in="cells" type="matrix"
            values="0 0 0 0 0.32
                    0 0 0 0 0.32
                    0 0 0 0 0.32
                    0 0 0 -2.2 1.35" result="cellTone"/>
          <feTurbulence type="fractalNoise" baseFrequency="0.85" numOctaves="2" seed="9" result="fine"/>
          <feColorMatrix in="fine" type="matrix"
            values="0 0 0 0 0.4
                    0 0 0 0 0.4
                    0 0 0 0 0.4
                    0 0 0 0.35 -0.1" result="fineTone"/>
          <feMerge>
            <feMergeNode in="cellTone"/>
            <feMergeNode in="fineTone"/>
          </feMerge>
        </filter>
      </defs>
      <rect class="grain-layer" width="1200" height="693" filter="url(#pebble-grain)" opacity="0.22"/>
    </svg>
    <div class="leather-vignette"></div>
    <section class="card-message">
      <p>Congratulations, you have purchased an exquisite exclusive item from<br>Kestrel Ridge Hides.</p>
      <p>Each item has been tailored to the last stitch; each piece is produced<br>under the eye of our expert artisan. Using best canning processes here<br>in Australia our leather never loses its colour.</p>
      <p>Alpaca leather is used for the vehicle seats and interiors luxury&nbsp; vehicles<br>including Valmont Motors and Ridgeway Auto.</p>
      <p>Alpaca leather though thinner and lighter weight than traditional hides<br>has a much higher tensile strength which means it won’t stretch and sag.</p>
      <p>Alpaca leather maintains it shape and makes up beautifully due to its<br>inherent tensile strength and suppleness . . . it feels so buttery soft!</p>
      <p class="sign-off">Proudly 100% Australian</p>
    </section>
  </main>
</body>
</html>
```